Lanternleaf take out menu

We need a take out menu design using our menu attached. Info to include would be our address: 7816 Brindlewood Hollow Pkwy #204, Lafayette, LA 70508. Phone number is 337-514-2960. website is www.lanternleafgrv.com.

Industry/Entity Type

Asian Restaurant

```html
<!DOCTYPE html>
<html lang="en">
<head>
<meta charset="utf-8">
<title>Lanternleaf Take Out Menu</title>
<link href="https://fonts.googleapis.com/css2?family=Tinos:wght@400;700&display=swap" rel="stylesheet">
<style>
  :root{
    --backdrop:#e4e4e4;
    --paper:#ffffff;
    --maroon:#5b0b12;
    --red:#d21f2b;
    --ink:#5a1618;
    --chili:#d62a1e;
    --photo-light:#f3e6d8;
    --photo-mid:#d9b48e;
    --photo-dark:#b07a4e;
  }
  *{margin:0;padding:0;box-sizing:border-box}
  html,body{width:1200px;height:1000px;overflow:hidden;background:var(--backdrop)}
  body{font-family:'Tinos',serif;color:var(--ink)}
  .menu{position:absolute;left:41px;top:138px;width:1118px;height:723px;background:var(--paper);display:flex}
  .panel{position:relative;width:559px;height:100%}

  /* left panel */
  .brand{position:absolute;left:127px;top:59px;width:300px;height:300px;border:6px solid var(--maroon);border-radius:50%;display:flex;align-items:center;justify-content:center}
  .brand-name{font-family:'Tinos',serif;font-weight:700;font-size:44px;color:var(--maroon);letter-spacing:1px}
  .story-title{position:absolute;left:0;width:500px;top:379px;text-align:center;font-size:16px;font-weight:700;color:var(--red);letter-spacing:.5px}
  .story{position:absolute;font-size:11px;line-height:14.2px;color:var(--ink)}
  .story span{display:block;white-space:nowrap}
  .story-intro{left:94px;top:412px}
  .story-taper{left:47px;width:400px;top:511px;text-align:center}
  .contact-band{position:absolute;left:0;top:670px;width:559px;height:32px;background:var(--maroon);color:#fff;text-align:center;font-size:7.5px;line-height:10px;padding-top:6px}
  .website{position:absolute;left:0;width:559px;top:706px;text-align:center;font-size:7.5px;color:var(--ink)}

  /* right panel */
  .section-band{position:absolute;left:0;top:34px;width:559px;height:43px;background:var(--maroon);color:#fff;text-align:center;font-size:11px;letter-spacing:4px;line-height:43px}
  .column{position:absolute;top:108px;width:210px}
  .column-left{left:25px}
  .column-right{left:305px;width:202px}
  .item{margin-bottom:14px}
  .item-head{display:flex;align-items:baseline;font-size:11.2px;font-weight:700;line-height:15px;text-transform:uppercase;color:var(--maroon)}
  .item-name{white-space:nowrap;display:flex;align-items:center;gap:2px}
  .leader{flex:1;border-bottom:1.2px dotted var(--maroon);margin:0 4px;transform:translateY(-3px)}
  .price{white-space:nowrap;font-weight:400}
  .item-head.wrap{display:block}
  .item-head.wrap .tail{display:flex;align-items:baseline}
  .desc{font-size:11px;line-height:13.5px;text-align:justify;color:var(--ink)}
  .chili{width:13px;height:11px;display:inline-block}
  .photo{position:absolute;left:280px;top:537px;width:279px;height:186px}
</style>
</head>
<body>
<main class="menu">
  <section class="panel panel-story">
    <div class="brand"><span class="brand-name">Lanternleaf</span></div>
    <h2 class="story-title">OUR STORY</h2>
    <div class="story story-intro">
      <span>At Lanternleaf, we pride ourselves in serving fresh, authentic Sichuan Chinese</span>
      <span>cuisine delicately prepared by our expertly trained Chefs.</span>
      <span>Sichuan cuisine originates from southwest China between the Sichuan Basin and</span>
      <span>Tibetan Plateau. It is known for being both very spicy and flavorful, much like</span>
      <span>our own southern Louisiana cuisine.</span>
      <span>Our Executive Chef, Wen Liao grew up in the southwestern Chinese province of</span>
      <span>Sichuan, China where he began his training at fifteen years old under his grand-</span>
    </div>
    <div class="story story-taper">
      <span>father's mentorship. Chef Liao became an acclaimed chef in his province,</span>
      <span>opening several restaurants and traveling throughout China to cater for many</span>
      <span>of China's elite. His dream was to share his Sichuan style with the world</span>
      <span>which lead him to the United States. He has worked in restaurants in</span>
      <span>both Houston and New York and we now welcome him to his new</span>
      <span>home in Lafayette, Louisiana.</span>
      <span>We are very excited to bring to Lafayette the authentici-</span>
      <span>ty of Chinese cuisine and hope you enjoy your</span>
      <span>experience dining with us.</span>
    </div>
    <footer class="contact-band">7816 Brindlewood Hollow Pkwy #204, Lafayette, LA 70508<br>337-514-2960</footer>
    <div class="website">www.lanternleafgrv.com</div>
  </section>

  <section class="panel panel-menu">
    <h2 class="section-band">APPETIZERS</h2>
    <svg width="0" height="0" style="position:absolute">
      <defs>
        <symbol id="chili" viewBox="0 0 13 11"><path d="M11.5 1.2c-.6 2.8-3.4 6.6-9.8 8.6-1 .3-1.1-.6-.2-.9 4.6-1.8 7.2-4.6 8.4-7.4z" fill="var(--chili)"/><path d="M10 2.2l1.5-1.4 1.2.3" stroke="#3c6b22" stroke-width="1" fill="none"/></symbol>
      </defs>
    </svg>
    <div class="column column-left">
      <div class="item"><div class="item-head"><span class="item-name">Edamame</span><span class="leader"></span><span class="price">$ 4</span></div><p class="desc">Seasoned &amp; boiled soy bean</p></div>
      <div class="item"><div class="item-head"><span class="item-name">Scallion Pancakes</span><span class="leader"></span><span class="price">$ 6</span></div><p class="desc">Traditional Chinese flatbread folded with oil and minced scallions and pan fried</p></div>
      <div class="item"><div class="item-head"><span class="item-name">Lanternleaf Lettuce Wraps</span><span class="leader"></span><span class="price">$ 8</span></div><p class="desc">Seasoned ground chicken drizzled with our top secret homemade sauce served with lettuce wraps</p></div>
      <div class="item"><div class="item-head"><span class="item-name">Salt &amp; Pepper Calamari</span><span class="leader"></span><span class="price">$ 9</span></div><p class="desc">Crispy Calamari with Green &amp; red peppers and onions</p></div>
      <div class="item"><div class="item-head"><span class="item-name">Buddha Bang Shrimp</span><span class="leader"></span><span class="price">$ 9</span></div><p class="desc">Crispy fried shrimp tossed in our creamy spicy sauce</p></div>
      <div class="item"><div class="item-head"><span class="item-name">Drunken Chicken <svg class="chili"><use href="#chili"/></svg></span><span class="leader"></span><span class="price">$ 8</span></div><p class="desc">Chicken, Thai chili in a house made spicy sauce</p></div>
      <div class="item"><div class="item-head"><span class="item-name">Sichuan Spiced Beef <svg class="chili"><use href="#chili"/></svg><svg class="chili"><use href="#chili"/></svg></span><span class="leader"></span><span class="price">$ 9</span></div><p class="desc">Beef Shank, beef tripe, cilantro, peanuts and celery</p></div>
      <div class="item"><div class="item-head"><span class="item-name">Beef Crispy Bottom Bao</span><span class="leader"></span><span class="price">$ 10</span></div><p class="desc">Pan fried crispy bottom Bao, stuffed with beef, drizzled with scallion and sesame (Fresh made to order, takes at least 20 mins to serve)</p></div>
      <div class="item"><div class="item-head wrap"><span class="item-name">Shrimp &amp; Beef Crispy Bottom</span><span class="tail"><span class="item-name">Bao</span><span class="leader"></span><span class="price">$ 10</span></span></div><p class="desc">Pan fried crispy bottom Bao, stuffed with beef and shrimp, drizzled with scallion and sesame (Fresh made to order, takes at least 20 mins to serve)</p></div>
    </div>
    <div class="column column-right">
      <div class="item"><div class="item-head"><span class="item-name">Crispy Mala Beef Jerky <svg class="chili"><use href="#chili"/></svg><svg class="chili"><use href="#chili"/></svg></span><span class="leader"></span><span class="price">$ 9</span></div><p class="desc">Dry fried shredded beef with various peppers in sesame and peppercorn oil</p></div>
      <div class="item"><div class="item-head"><span class="item-name">Fried Chicken Dumplings (6)</span><span class="leader"></span><span class="price">$ 6</span></div><p class="desc">Chinese dumpling stuffed with Chicken, Shiitake mushrooms and bamboo shoots</p></div>
      <div class="item"><div class="item-head"><span class="item-name">Red Oil Dumplings (6) <svg class="chili"><use href="#chili"/></svg></span><span class="leader"></span><span class="price">$ 7</span></div><p class="desc">Pork filled dumplings in Sichuan red oil sauce drizzled with sesame</p></div>
      <div class="item"><div class="item-head"><span class="item-name">Pork Egg Rolls (2)</span><span class="leader"></span><span class="price">$ 4</span></div><p class="desc">Hand rolled with julienned veggies with our sweet n' sour mustard sauce</p></div>
      <div class="item"><div class="item-head"><span class="item-name">Vegetarian Spring Rolls (3)</span><span class="leader"></span><span class="price">$ 4</span></div><p class="desc">Traditional Asian Roll served with a sweet chili sauce</p></div>
      <div class="item"><div class="item-head"><span class="item-name">Garlic Cucumber Salad</span><span class="leader"></span><span class="price">$ 7</span></div><p class="desc">Sliced cucumber with a garlic vinaigrette</p></div>
      <div class="item"><div class="item-head"><span class="item-name">Hot N' Sour Soup <svg class="chili"><use href="#chili"/></svg></span><span class="leader"></span><span class="price">$ 4</span></div><p class="desc">Tangy broth with Bamboo shoot, wood ear fungus, tofu, egg and carrots</p></div>
      <div class="item"><div class="item-head"><span class="item-name">West Lake Soup</span><span class="leader"></span><span class="price">$ 4</span></div><p class="desc">Light creamy soup with ground beef, diced Shiitake mushroom, tofu, bamboo shoots, egg white and cilantro</p></div>
    </div>
    <svg class="photo" viewBox="0 0 279 186" role="img" aria-label="Photo of crispy fried wontons on a white plate">
      <defs>
        <linearGradient id="photoTone" x1="0" y1="1" x2="1" y2="0">
          <stop offset="0" stop-color="var(--photo-light)"/>
          <stop offset=".55" stop-color="var(--photo-mid)"/>
          <stop offset="1" stop-color="var(--photo-dark)"/>
        </linearGradient>
      </defs>
      <path d="M0 52 C90 44 190 30 279 0 L279 186 L0 186 Z" fill="url(#photoTone)"/>
    </svg>
  </section>
</main>
</body>
</html>
```